Business card design needed

It's a new business in town.Something so the name stands out.I need a logo for the B.R.W
I may all so use the design as a sign on a building

Contact Information for Business Card

B.R.W
Brindlewood Auto Detailing
42 Fenwarra Crs
Brindlewood Vic 3799
Ph:(03)59284736
Mob:0417362958

```html
<!DOCTYPE html>
<html lang="en">
<head>
<meta charset="utf-8">
<title>B.R.W Brindlewood Auto Detailing – Business Card</title>
<link rel="stylesheet" href="https://fonts.googleapis.com/css2?family=PT+Sans+Narrow:wght@700&display=swap">
<style>
  :root {
    --ink: #0b0b0b;
    --bg-light: #ffffff;
    --bg-mid: #eceded;
    --bg-dark: #cfd2d3;
    --skyline-top: #2a2a2a;
    --skyline-bottom: #000000;
  }
  html, body {
    margin: 0;
    padding: 0;
    width: 1200px;
    height: 691px;
    overflow: hidden;
    background: var(--bg-light);
  }
  .card {
    position: relative;
    width: 1200px;
    height: 691px;
    overflow: hidden;
    background: linear-gradient(250deg, var(--bg-light) 0%, var(--bg-mid) 40%, var(--bg-dark) 100%);
    font-family: "PT Sans Narrow", "Arial Narrow", sans-serif;
    font-weight: 700;
    color: var(--ink);
  }
  .brand-name {
    position: absolute;
    left: 80px;
    top: 96px;
    margin: 0;
    font-size: 92px;
    line-height: 1;
    letter-spacing: 2px;
  }
  .business-title {
    position: absolute;
    left: 492px;
    top: 88px;
    margin: 0;
    font-size: 47px;
    line-height: 1.1;
    white-space: nowrap;
  }
  .contact {
    position: absolute;
    left: 676px;
    top: 280px;
    width: 400px;
    margin: 0;
    font-style: normal;
    text-align: center;
    font-size: 47px;
    line-height: 67.5px;
    white-space: nowrap;
  }
  .contact span { display: block; }
  .skyline {
    position: absolute;
    left: 0;
    bottom: 0;
    width: 1200px;
    height: 148px;
    display: block;
  }
</style>
</head>
<body>
  <main class="card">
    <p class="brand-name">B.R.W</p>
    <h1 class="business-title">B.R.W Brindlewood Auto Detailing</h1>
    <address class="contact">
      <span class="contact-street">42 Fenwarra Crs</span>
      <span class="contact-town">Brindlewood Vic 3799</span>
      <span class="contact-phone">Ph:(03)59284736</span>
      <span class="contact-mobile">Mob:0417362958</span>
    </address>
    <svg class="skyline" viewBox="0 0 1200 148" preserveAspectRatio="none" role="img" aria-label="Black silhouette of a city skyline with towers and high-rise buildings along the bottom of the card">
      <defs>
        <linearGradient id="skyline-fill" x1="0" y1="0" x2="0" y2="1">
          <stop offset="0" stop-color="var(--skyline-top)"/>
          <stop offset="1" stop-color="var(--skyline-bottom)"/>
        </linearGradient>
      </defs>
      <rect x="0" y="0" width="1200" height="148" fill="url(#skyline-fill)"/>
    </svg>
  </main>
</body>
</html>
```